Book Cover Design

Design with title UNWAVERING
Subtitle: Ways to Kindle the Spark of Resolve
Author Name: Carla Jean Morrow
Put DAILY MERIDIAN BESTSELLER at top
Shimmer design, see inspirational images attached

```html
<!DOCTYPE html>
<html lang="en">
<head>
<meta charset="UTF-8">
<title>Unwavering — Book Cover</title>
<link href="https://fonts.googleapis.com/css2?family=Exo+2:ital,wght@1,800;1,900&family=Montserrat:ital,wght@0,400;0,500;0,700;0,800;1,800&display=swap" rel="stylesheet">
<style>
  :root {
    --backdrop: #a7b5bb;
    --ink: #141414;
    --foil-white: #f6f7f8;
    --foil-pink: #f3d9e6;
    --foil-lilac: #d6d4f0;
    --foil-blue: #a9c8ee;
    --foil-teal: #6fe3d4;
    --foil-yellow: #f5e98a;
    --foil-mint: #c9f0e6;
  }
  * { margin: 0; padding: 0; box-sizing: border-box; }
  html, body {
    width: 1200px;
    height: 900px;
    overflow: hidden;
    background: var(--backdrop);
  }
  .canvas {
    position: relative;
    width: 1200px;
    height: 900px;
  }
  .cover {
    position: absolute;
    left: 356px;
    top: 40px;
    width: 488px;
    height: 820px;
    overflow: hidden;
    background:
      radial-gradient(ellipse 140px 110px at 86% 86%, var(--foil-yellow) 0%, rgba(245,233,138,0) 100%),
      radial-gradient(ellipse 180px 160px at 80% 70%, var(--foil-teal) 0%, rgba(111,227,212,0) 100%),
      radial-gradient(ellipse 200px 180px at 20% 72%, var(--foil-blue) 0%, rgba(169,200,238,0) 100%),
      radial-gradient(ellipse 180px 140px at 12% 50%, var(--foil-pink) 0%, rgba(243,217,230,0) 100%),
      radial-gradient(ellipse 200px 130px at 60% 56%, var(--foil-lilac) 0%, rgba(214,212,240,0) 100%),
      radial-gradient(ellipse 220px 160px at 75% 28%, var(--foil-mint) 0%, rgba(201,240,230,0) 100%),
      linear-gradient(180deg, var(--foil-white) 0%, #eef0f4 55%, #dfe6ee 100%);
  }
  .bestseller-line {
    position: absolute;
    top: 44px;
    left: 0;
    width: 100%;
    text-align: center;
    font-family: "Montserrat", sans-serif;
    font-style: italic;
    font-weight: 800;
    font-size: 16px;
    letter-spacing: 2.6px;
    color: var(--ink);
  }
  .title {
    position: absolute;
    top: 290px;
    left: 0;
    width: 100%;
    text-align: center;
    font-family: "Exo 2", sans-serif;
    font-style: italic;
    font-weight: 900;
    font-size: 58px;
    letter-spacing: 1px;
    line-height: 1;
    color: var(--ink);
  }
  .title .initial { font-size: 70px; }
  .subtitle {
    position: absolute;
    top: 385px;
    left: 0;
    width: 100%;
    font-family: "Montserrat", sans-serif;
    font-size: 23px;
    line-height: 1;
    color: var(--ink);
    text-transform: uppercase;
  }
  .subtitle strong { font-weight: 800; }
  .subtitle-row {
    display: flex;
    justify-content: center;
    align-items: center;
    gap: 10px;
    font-weight: 500;
  }
  .subtitle-row + .subtitle-row { margin-top: 10px; }
  .rule {
    display: block;
    width: 40px;
    height: 2px;
    background: var(--ink);
  }
  .subtitle-row.underlined span.text {
    padding-bottom: 6px;
    border-bottom: 2px solid var(--ink);
  }
  .author {
    position: absolute;
    top: 758px;
    left: 0;
    width: 100%;
    text-align: center;
    font-family: "Montserrat", sans-serif;
    font-weight: 400;
    font-size: 15px;
    color: var(--ink);
  }
</style>
</head>
<body>
  <main class="canvas">
    <section class="cover">
      <p class="bestseller-line">DAILY MERIDIAN BESTSELLER</p>
      <h1 class="title"><span class="initial">U</span>NWAVERING</h1>
      <div class="subtitle">
        <div class="subtitle-row">
          <span class="rule"></span>
          <span class="text">Ways to <strong>Kindle</strong></span>
          <span class="rule"></span>
        </div>
        <div class="subtitle-row underlined">
          <span class="text">The <strong>Spark</strong> of <strong>Resolve</strong></span>
        </div>
      </div>
      <p class="author">Carla Jean Morrow</p>
    </section>
  </main>
</body>
</html>
```